Website for Verdix Partners

We need to create a website for our company. Attached is the site map of the website and data input needed. Our theme colour is RED and our Logo is attached

We need a very attractive design where graphics are largely used like flash.

The main idea of the website is to show Telecommunications Suppliers World Wide that we could assist them in getting more business in Africa and Middle East through our local presence in this region.

Target Market(s)

Telecommunication Suppliers and Clients

Industry/Entity Type

Business

Font styles to use
Serif
Sans Serif

Colors
ec2027

Requirements
Must have
• Graphics that shows Telecommunications Suppliers World Wide that we could assist them in getting more business in Africa and Middle East through our local presence in this region.

The website should be easy to edit for future changes by us.
Nice to have
• New ideas

```html
<!DOCTYPE html>
<html lang="en">
<head>
<meta charset="utf-8">
<title>Verdix Partners</title>
<link href="https://fonts.googleapis.com/css2?family=Josefin+Sans:wght@200;300;700&family=Arimo:wght@400;700&display=swap" rel="stylesheet">
<style>
  :root {
    --red: #e11b24;
    --red-dark: #c4141c;
    --ink: #2b2b2b;
    --hero-dark: #1c1c1c;
    --grey-band: #e2e2e2;
    --paper: #fbfbfb;
    --muted: #8a8a8a;
    --soft-pink: #f3c9cb;
  }
  * { box-sizing: border-box; margin: 0; padding: 0; }
  html, body { width: 1200px; height: 2340px; overflow: hidden; }
  body { position: relative; font-family: "Arimo", Arial, sans-serif; background: var(--paper); color: var(--ink); }
  .abs { position: absolute; }

  /* Hero */
  .hero { position: absolute; left: 0; top: 0; width: 1200px; height: 630px; overflow: hidden; }
  .hero-bg { position: absolute; inset: 0; background: radial-gradient(ellipse at 48% 42%, #4a4a4a 0%, #2c2c2c 40%, var(--hero-dark) 80%); }
  .brand { position: absolute; left: 50px; top: 24px; display: flex; align-items: center; gap: 14px; }
  .brand-mark { width: 30px; height: 30px; background: var(--red); }
  .brand-name { font-family: "Arimo", Arial, sans-serif; font-size: 30px; color: #6d6d6d; letter-spacing: 1px; text-transform: uppercase; }
  .main-nav { position: absolute; top: 22px; left: 660px; display: flex; gap: 0; }
  .main-nav a { position: absolute; font-size: 17px; font-weight: 700; color: var(--red); text-decoration: none; white-space: nowrap; }
  .main-nav a.active { color: #fff; border: 1px solid #777; border-bottom: 2px solid #aaa; padding: 2px 10px 4px; }
  .headline-1 { position: absolute; left: 173px; top: 152px; font-family: "Josefin Sans", sans-serif; font-size: 54px; line-height: 1; color: var(--red); white-space: nowrap; }
  .headline-1 .thin { font-weight: 200; }
  .headline-1 .bold { font-weight: 700; }
  .headline-2 { position: absolute; left: 634px; top: 230px; font-family: "Josefin Sans", sans-serif; font-weight: 200; font-size: 48px; line-height: 1; color: var(--red); }
  .headline-3 { position: absolute; left: 632px; top: 274px; font-family: "Josefin Sans", sans-serif; font-weight: 700; font-size: 58px; line-height: 1; color: var(--red); }
  .tagline { position: absolute; left: 637px; top: 336px; width: 290px; font-size: 17px; font-weight: 700; line-height: 20px; color: var(--muted); }
  .video { position: absolute; left: 179px; top: 280px; width: 367px; height: 257px; border: 2px solid var(--red); background: linear-gradient(135deg, #f4f4f4 0%, #d8dde3 45%, #39414e 70%, #eeeeee 100%); }
  .play { position: absolute; left: 238px; top: 340px; }
  .slider-arrow { position: absolute; top: 296px; }

  /* Who we are */
  .who { position: absolute; left: 0; top: 630px; width: 1200px; height: 363px; background: var(--red); }
  .section-title { position: absolute; left: 0; width: 1200px; text-align: center; font-size: 40px; font-weight: 400; }
  .who .section-title { top: 72px; color: #f6d2d3; }
  .who-text { position: absolute; left: 227px; top: 142px; width: 790px; font-size: 20px; line-height: 24px; color: #fbe3e4; }

  /* Portfolio */
  .portfolio { position: absolute; left: 0; top: 993px; width: 1200px; height: 593px; background: var(--grey-band); }
  .portfolio .section-title { top: 20px; color: var(--ink); }
  .card { position: absolute; top: 164px; width: 274px; height: 255px; }
  .card-label { position: absolute; left: 0; top: 0; width: 100%; height: 38px; background: var(--red); color: #fff; font-size: 17px; padding: 9px 10px 0; }
  .card-photo { position: absolute; left: 0; top: 38px; width: 100%; height: 217px; }
  .photo-phone { background: linear-gradient(140deg, #0c0c0c 0%, #3a3a3a 45%, #9a9a9a 70%, #222 100%); }
  .photo-meeting { background: linear-gradient(180deg, #c8c2b8 0%, #8a8478 45%, #2a2a2e 80%, #4a4a4e 100%); }
  .photo-chain { background: linear-gradient(160deg, #efe4cc 0%, #d7b56e 45%, #e7c020 70%, #8a7a60 100%); }
  .card-cut { position: absolute; right: 0; top: 0; }
  .view-all { position: absolute; left: 522px; top: 475px; font-size: 17px; color: #111; }
  .view-all span { color: var(--red); }

  /* Footprint */
  .footprint { position: absolute; left: 0; top: 1586px; width: 1200px; height: 754px; background: var(--paper); }
  .footprint .section-title { top: 76px; font-size: 34px; color: var(--ink); }
  .footprint-text { position: absolute; left: 352px; top: 193px; width: 540px; font-size: 18px; line-height: 23px; color: #222; }
  .map-frame { position: absolute; left: 373px; top: 320px; width: 461px; height: 290px; border: 1px solid #ea8d91; background: #fff; padding: 22px 18px; }
  .map { width: 100%; height: 100%; background: linear-gradient(90deg, #0c4a93 0%, #2b66ad 30%, #f08a0c 55%, #f6b21a 80%, #f2c44a 100%); border-radius: 40px 60px 30px 50px; }
</style>
</head>
<body>

<section class="hero">
  <div class="hero-bg" role="img" aria-label="Dark moody photo of a small cardboard robot figure on a textured surface"></div>

  <div class="brand">
    <span class="brand-mark"></span>
    <span class="brand-name">Verdix Partners</span>
  </div>

  <nav class="main-nav">
    <a class="active" href="#" style="left:0;top:0">home</a>
    <a href="#" style="left:89px;top:5px">company</a>
    <a href="#" style="left:195px;top:5px">portfolio</a>
    <a href="#" style="left:294px;top:5px">footprint</a>
    <a href="#" style="left:395px;top:5px">contact us</a>
  </nav>

  <h1 class="headline-1"><span class="thin">YOUR·</span><span class="bold">CHALLENGE</span></h1>
  <svg class="abs" style="left:180px;top:198px" width="650" height="30" aria-hidden="true">
    <line x1="6" y1="16" x2="620" y2="16" stroke="#e11b24" stroke-width="2"/>
    <circle cx="632" cy="14" r="11" fill="none" stroke="#e11b24" stroke-width="2"/>
    <path d="M626 14h12M632 8v12" stroke="#e11b24" stroke-width="2"/>
  </svg>
  <p class="headline-2">IS OUR</p>
  <p class="headline-3">BUSINESS</p>
  <p class="tagline">Becoming the service partner of choice for Communication &amp; Information technology services</p>

  <div class="video" role="img" aria-label="Video still of a businessman celebrating with raised fists"></div>
  <svg class="play" width="86" height="86" aria-hidden="true">
    <circle cx="43" cy="43" r="40" fill="#2e2e2e" fill-opacity="0.85" stroke="#6a6a6a" stroke-width="4"/>
    <path d="M33 26 L60 43 L33 60 Z" fill="#9a9a9a"/>
  </svg>

  <svg class="slider-arrow" style="left:24px" width="60" height="70" aria-hidden="true">
    <polyline points="28,4 4,32 28,60" fill="none" stroke="#dcdcdc" stroke-width="2"/>
    <line x1="22" y1="36" x2="54" y2="66" stroke="#e11b24" stroke-width="4"/>
  </svg>
  <svg class="slider-arrow" style="left:1110px" width="60" height="70" aria-hidden="true">
    <polyline points="30,4 54,32 30,60" fill="none" stroke="#dcdcdc" stroke-width="2"/>
    <line x1="36" y1="36" x2="4" y2="66" stroke="#e11b24" stroke-width="4"/>
  </svg>
</section>

<section class="who">
  <h2 class="section-title">Who We Are</h2>
  <p class="who-text">Verdix Partners is a leading telecommunication Solution Provider; the company provides state of the art technologies and turnkey solutions to its clients that fully support their business needs from planning right through full operation</p>
  <svg class="abs" style="left:395px;top:252px" width="410" height="30" aria-hidden="true">
    <line x1="0" y1="14" x2="186" y2="14" stroke="#fff" stroke-width="1.5"/>
    <line x1="214" y1="14" x2="406" y2="14" stroke="#fff" stroke-width="1.5"/>
    <circle cx="200" cy="14" r="12" fill="none" stroke="#fff" stroke-width="2"/>
    <path d="M194 14h12M200 8v12" stroke="#fff" stroke-width="2"/>
  </svg>
</section>

<section class="portfolio">
  <h2 class="section-title">Our Portfolio Showcase</h2>
  <svg class="abs" style="left:425px;top:87px" width="340" height="30" aria-hidden="true">
    <line x1="0" y1="14" x2="156" y2="14" stroke="#555" stroke-width="1.5"/>
    <line x1="182" y1="14" x2="336" y2="14" stroke="#555" stroke-width="1.5"/>
    <circle cx="169" cy="14" r="12" fill="none" stroke="#e11b24" stroke-width="2"/>
    <path d="M163 14h12M169 8v12" stroke="#e11b24" stroke-width="2"/>
  </svg>

  <article class="card" style="left:196px">
    <div class="card-label">Managed Services</div>
    <div class="card-photo photo-phone" role="img" aria-label="Black and white photo of a hand holding a smartphone showing a news app"></div>
  </article>
  <article class="card" style="left:471px">
    <div class="card-label">Business Consultancy</div>
    <div class="card-photo photo-meeting" role="img" aria-label="Photo of business people shaking hands in front of a classical building"></div>
  </article>
  <article class="card" style="left:747px">
    <div class="card-photo photo-chain" role="img" aria-label="Photo of small cardboard figures with a heap of yellow chain"></div>
    <div class="card-label">Value Added Service</div>
    <svg class="card-cut" width="40" height="80" aria-hidden="true">
      <polygon points="0,0 40,0 40,76" fill="#e11b24"/>
    </svg>
  </article>

  <p class="view-all">view <span>all our work</span></p>
  <svg class="abs" style="left:475px;top:482px" width="275" height="30" aria-hidden="true">
    <line x1="0" y1="14" x2="243" y2="14" stroke="#333" stroke-width="1.5"/>
    <circle cx="255" cy="14" r="11" fill="none" stroke="#e11b24" stroke-width="2"/>
    <path d="M249 14h12M255 8v12" stroke="#e11b24" stroke-width="2"/>
  </svg>
</section>

<section class="footprint">
  <h2 class="section-title">Footprint</h2>
  <svg class="abs" style="left:395px;top:122px" width="410" height="30" aria-hidden="true">
    <line x1="0" y1="14" x2="186" y2="14" stroke="#e11b24" stroke-width="1.5"/>
    <line x1="212" y1="14" x2="406" y2="14" stroke="#e11b24" stroke-width="1.5"/>
    <circle cx="199" cy="14" r="12" fill="none" stroke="#e11b24" stroke-width="2"/>
    <path d="M193 14h12M199 8v12" stroke="#e11b24" stroke-width="2"/>
  </svg>
  <p class="footprint-text">Our Head office in UK and we cover Middle East and Africa thorough a large and strong group of local footprint</p>
  <div class="map-frame">
    <div class="map" role="img" aria-label="World map highlighting the Americas in blue and Europe, Africa, Middle East and Asia in orange"></div>
  </div>
</section>

</body>
</html>
```